Flyer für Beratung rund um den Computer
Zielgruppe
Hauptsächlich: Beratung rund um den Computer, individuelle Schulungen, technische Hilfe . Aber auch: Einführung in die Programmierung, Webseitenerstellung etc. Zielgruppe sind Privatpersonen, gerne auch ältere Personen, alle die sich unsicher im Umgang mit Computern fühlen und freundliche, geduldige Hilfe suchen.
Aufgabenstellung
Da meine Zielgruppe eher keine Computerfreaks sind, sollte der Flyer nicht zu technisch aussehen, sondern für Hilfesuchende ansprechend und freundlich wirken.

```html
<!DOCTYPE html>
<html lang="de">
<head>
<meta charset="utf-8">
<title>Computerhilfe Flyer</title>
<link href="https://fonts.googleapis.com/css2?family=Arimo:wght@400;700&family=Montserrat:wght@700&display=swap" rel="stylesheet">
<style>
  :root {
    --bg: #424d3d;
    --green: #6fbe44;
    --slate: #54575a;
    --slate-text: #55585b;
    --white: #ffffff;
  }
  * { box-sizing: border-box; margin: 0; padding: 0; }
  html, body { width: 1200px; height: 1200px; overflow: hidden; }
  body { background: var(--bg); font-family: "Arimo", Arial, sans-serif; position: relative; }

  .flyer {
    position: absolute;
    background: var(--white);
    box-shadow: 4px 6px 10px rgba(0,0,0,0.35);
    overflow: hidden;
  }
  .flyer-front { left: 21px; top: 17px; width: 555px; height: 777px; }
  .flyer-back { left: 622px; top: 229px; width: 552px; height: 776px; }

  /* front */
  .headline-band {
    position: absolute; left: 0; top: 0; width: 100%; height: 113px;
    background: var(--green);
    padding: 22px 24px 0;
  }
  .headline {
    font-family: "Montserrat", Arial, sans-serif;
    font-weight: 700; color: var(--white);
    font-size: 26px; line-height: 28px; letter-spacing: 0.3px;
  }
  .photo-help {
    position: absolute; left: 0; top: 113px; width: 100%; height: 374px;
    background: linear-gradient(135deg, #8c9196 0%, #b8bcbf 35%, #6e6f70 65%, #3a3b3c 100%);
  }
  .info-panel {
    position: absolute; left: 0; top: 487px; width: 100%; height: 218px;
    background: var(--slate); color: var(--white);
  }
  .info-lead {
    position: absolute; left: 27px; top: 8px; width: 510px;
    font-weight: 700; font-size: 17.5px; line-height: 21.5px;
  }
  .contact {
    position: absolute; left: 0; top: 85px; width: 100%;
    text-align: center; font-weight: 700; font-size: 15px; line-height: 18.4px;
    white-space: nowrap;
  }

  /* brand strip */
  .brand-strip {
    position: absolute; left: 0; bottom: 0; width: 100%; height: 72px;
    background: var(--white);
    display: flex; align-items: center; justify-content: space-around;
    padding: 0 18px;
  }
  .brand { font-weight: 700; font-size: 14px; color: var(--slate-text); }

  /* back */
  .photo-desk {
    position: absolute; left: 0; top: 0; width: 100%; height: 320px;
    background: linear-gradient(160deg, #8a7260 0%, #6b5444 45%, #a08a78 75%, #5e4a3c 100%);
  }
  .service-banner { position: absolute; left: 0; top: 0; width: 552px; height: 160px; }
  .service-banner text {
    font-family: "Arimo", Arial, sans-serif; font-size: 27px; fill: var(--white);
  }
  .offer-panel {
    position: absolute; left: 0; top: 320px; width: 100%; height: 247px;
    background: var(--slate); color: var(--white);
  }
  .offer-title {
    position: absolute; left: 22px; top: 7px;
    font-weight: 700; font-size: 17.5px;
  }
  .offer-list { position: absolute; left: 33px; top: 41px; list-style: none; font-size: 16.5px; }
  .offer-list li { line-height: 21.5px; }
  .offer-list .bullet { display: inline-block; width: 11px; }
  .offer-list .gap-top { margin-top: 6.5px; }
  .offer-list .sub { padding-left: 11px; }

  .service-panel {
    position: absolute; left: 0; top: 567px; width: 100%; height: 136px;
    background: var(--green);
    padding: 26px 0 0 58px;
  }
  .service-row {
    display: flex; justify-content: space-between; width: 432px;
    font-weight: 700; font-size: 15.5px; line-height: 22.3px;
  }
  .service-name { color: var(--slate-text); }
  .service-note { color: var(--white); }
</style>
</head>
<body>

<section class="flyer flyer-front">
  <div class="headline-band">
    <h1 class="headline">Genieße die Sonne und lass<br>uns deine technischen Sorgen<br>übernehmen</h1>
  </div>
  <div class="photo-help" role="img" aria-label="Foto: junger Mann hilft einem älteren Herrn mit Brille am Laptop in einer Küche"></div>
  <div class="info-panel">
    <p class="info-lead">Sie sind unsicher im Umgang mit einem Computer und brauchen Hilfe ? Ich helfe Ihnen.</p>
    <p class="contact">Kontakt:<br>Lorem ipsum dolor sit amet, consectetuer adipiscing elit, sed diam<br>nonummy nibh euismod tincidunt ut laoreet dolore magna aliquam<br>erat volutpat. Ut wisi enim ad minim veniam, quis nostrud exerci<br>tation ullamcorper suscipit lobortis nisl ut aliquip ex ea commodo<br>consequat. Duis autem vel eum iriure dolor in hendrerit in vul</p>
  </div>
  <div class="brand-strip">
    <span class="brand">Kordel</span>
    <span class="brand">Vantor</span>
    <span class="brand">Lumbra</span>
    <span class="brand">Ostek</span>
    <span class="brand">Brimo</span>
    <span class="brand">Quell</span>
    <span class="brand">Fenwa</span>
    <span class="brand">Tarvis</span>
  </div>
</section>

<section class="flyer flyer-back">
  <div class="photo-desk" role="img" aria-label="Foto: Laptop, Notizblock mit Stift, Wasserglas, Smartphone und Pflanze auf einem Holztisch"></div>
  <svg class="service-banner" viewBox="0 0 552 160">
    <polygon points="0,88 388,0 552,0 552,19 0,146" fill="#54575a"/>
    <line x1="0" y1="147" x2="552" y2="20" stroke="#ffffff" stroke-width="4"/>
    <text x="22" y="124" transform="rotate(-12.8 22 124)">Computerhilfe - Beratung - Reparatur</text>
  </svg>
  <div class="offer-panel">
    <h2 class="offer-title">SIE haben probleme mit Ihrem Computer ?</h2>
    <ul class="offer-list">
      <li><span class="bullet">•</span>Wir bringen Ihren Computer wieder zum laufen</li>
      <li class="gap-top"><span class="bullet"></span>Wir beraten Sie rund um den Computer</li>
      <li class="gap-top"><span class="bullet">•</span>Wir führen individuelle Schulungen durch, z.b.</li>
      <li class="sub">- Sicher umgang mit Emails (worauf sollte ich achten)</li>
      <li class="sub">- Was kann ich mit dem Schreibprogramm</li>
      <li class="sub">- Bildbearbeitung und vieles mehr</li>
      <li class="gap-top"><span class="bullet">•</span>Wir bieten technische Hilfe</li>
      <li class="gap-top"><span class="bullet">•</span>Einführung in die Programmierung, Webseitenerstellung</li>
    </ul>
  </div>
  <div class="service-panel">
    <div class="service-row"><span class="service-name">Fachwerkstatt</span><span class="service-note">...für alle Marken &amp; alle Hersteller</span></div>
    <div class="service-row"><span class="service-name">Verkauf &amp; Beratung</span><span class="service-note">...freundlich, fair und kompetent</span></div>
    <div class="service-row"><span class="service-name">Vor-Ort-Service</span><span class="service-note">...egal ob Privat- oder Firmenkunde</span></div>
    <div class="service-row"><span class="service-name">Datensicherung</span><span class="service-note">...egal ob lokal oder online</span></div>
  </div>
  <div class="brand-strip">
    <span class="brand">Kordel</span>
    <span class="brand">Vantor</span>
    <span class="brand">Lumbra</span>
    <span class="brand">Ostek</span>
    <span class="brand">Brimo</span>
    <span class="brand">Quell</span>
    <span class="brand">Fenwa</span>
    <span class="brand">Tarvis</span>
  </div>
</section>

</body>
</html>
```